Health insurance Facts Infographic

We need an infographic compiling the research in the attached report. Can cover all topics in the report, or a few. It needs to be easy for our readers to understand and should follow the design guide/ color scheme laid out in our website www.covernook.com and attached infographic

Requirements
Must have
• • An estimated 27.5 million people, 8.5% of the population, went without health insurance in 2018. That was an increase of 1.9 million uninsured people, or 0.5 percentage point.
In 2017, the number of people without health insurance increased to 28.0 million, up from 27.3 million the year before, according to the latest Civic Household Census data released today.
• Working-age adults made up a much larger share of the uninsured population than any other age group. In fact, most uninsured people (84.6 percent) were 19- to 64-year-olds.
• The two largest groups in that age range are 26- to 34-year-olds and 35- to 44-year-olds. About 1 in 4 uninsured people were 26 to 34 years old, and about 1 in 5 people ages 34 to 44.
• Over half of all people without health insurance coverage were male (54.6 percent), even though the U.S. population has more women than men.
• About 4 in 10 uninsured people were non-Hispanic white, while nearly 6 in 10 people in the United States were non-Hispanic white.
• Other races and ethnic groups made up the majority of the uninsured population but less than half (39.3 percent) of the total population.
• The uninsured were disproportionately concentrated in the South.
Nice to have
• other supporting facts. Graphics maybe of people or bodies showing the statistics.

```html
<!DOCTYPE html>
<html lang="en">
<head>
<meta charset="utf-8">
<title>Covernook – Health Insurance Facts</title>
<link rel="stylesheet" href="https://fonts.googleapis.com/css2?family=Montserrat:wght@300;600;700;800;900&family=Lora:wght@400;600&family=Oswald:wght@600&display=swap">
<style>
  :root{
    --navy:#1c3547;
    --ink:#1a2a36;
    --orange:#e8532b;
    --sky:#2fb7f0;
    --sky-pale:#c9efff;
    --teal-a:#5ff3de;
    --teal-b:#16d3b4;
    --white:#ffffff;
    --box-line:#d6d6d6;
  }
  *{margin:0;padding:0;box-sizing:border-box}
  html,body{width:1200px;height:3959px;overflow:hidden;background:var(--white)}
  .infographic{position:relative;width:1200px;height:3959px;overflow:hidden;background:var(--white);font-family:"Montserrat",Arial,sans-serif;color:var(--ink)}
  .abs{position:absolute}
  .header-bg{left:0;top:0}
  .brand{left:60px;top:52px;font-size:66px;font-weight:700;color:#111;letter-spacing:-1px}
  .headline{left:62px;top:210px;font-size:60px;font-weight:900;line-height:57px;color:var(--navy);text-transform:uppercase;letter-spacing:.5px}
  .subtitle{left:62px;top:466px;font-family:"Lora",Georgia,serif;font-size:27px;line-height:32px;color:var(--navy)}
  .art{border-radius:24px}
  .num{font-size:150px;font-weight:300;line-height:150px;color:transparent;-webkit-text-stroke:2.5px var(--orange)}
  .rule{height:3px;background:var(--orange)}
  .rule::after{content:"";position:absolute;right:-6px;top:-5px;width:13px;height:13px;border-radius:50%;background:var(--orange)}
  .fact{font-size:26px;font-weight:700;line-height:36px;color:var(--ink);white-space:nowrap}
  .fact em{font-style:normal;color:var(--orange)}
  .note{font-family:"Lora",Georgia,serif;font-size:21px;line-height:24px;color:#2a2a2a;white-space:nowrap}
  .note b{font-weight:600}
  .teal-band{left:0;top:1597px;width:1200px;height:415px;background:linear-gradient(90deg,var(--teal-a),var(--teal-b))}
  .stat-box{width:392px;height:324px;border:2px solid var(--box-line);background:var(--white);text-align:center}
  .stat-box .lead{margin-top:22px;font-size:27px;font-weight:800;color:var(--navy)}
  .stat-box .big{margin-top:10px;height:108px;background:var(--orange);color:var(--white);font-family:"Oswald",Impact,sans-serif;font-weight:600;font-size:102px;line-height:108px;letter-spacing:-1px}
  .stat-box .tail{margin-top:20px;font-size:26px;font-weight:800;line-height:34px;color:var(--navy);white-space:nowrap}
  .vs{left:540px;top:2760px;width:120px;text-align:center;font-family:"Oswald",Impact,sans-serif;font-size:84px;color:#d9d9d9}
  .closing{left:0;top:3730px;width:1200px;text-align:center;font-size:40px;font-weight:900;line-height:53px;color:#111;text-transform:uppercase;white-space:nowrap}
</style>
</head>
<body>
<main class="infographic">

  <svg class="abs header-bg" width="1200" height="760" viewBox="0 0 1200 760" aria-hidden="true">
    <defs>
      <linearGradient id="skyGrad" x1="0" y1="0" x2="1" y2="1">
        <stop offset="0" stop-color="#55c9f6"/>
        <stop offset="1" stop-color="#1aa9ee"/>
      </linearGradient>
    </defs>
    <path d="M0 0H1200V560C1080 640 980 520 840 600C720 670 620 700 480 640C340 580 200 560 0 600Z" fill="url(#skyGrad)"/>
    <path d="M0 560C180 520 330 560 470 620C330 600 180 600 0 640Z" fill="var(--sky-pale)" opacity=".7"/>
  </svg>

  <div class="abs brand">covernook</div>
  <h1 class="abs headline">Life can get<br>complicated,<br>insuring it<br>shouldn’t be.</h1>
  <p class="abs subtitle">Easily find the right insurance<br>options to fit your life.</p>
  <div class="abs art" role="img" aria-label="Illustration of a patient and doctor beside a large medical clipboard with a shield and heart" style="left:660px;top:150px;width:420px;height:490px;background:linear-gradient(160deg,#3e5fd6,#7fd3f7)"></div>

  <!-- Fact 1 -->
  <div class="abs art" role="img" aria-label="Illustration of a person reading a long insurance document beside coins, a calculator and a pen" style="left:54px;top:635px;width:450px;height:420px;background:linear-gradient(160deg,#eef0f2,#c9ccd2)"></div>
  <div class="abs num" style="left:585px;top:594px">1</div>
  <div class="abs rule" style="left:562px;top:723px;width:350px"></div>
  <p class="abs fact" style="left:562px;top:755px">An estimated <em>27.5 million</em> people,<br><em>8.5%</em> of the population, went without<br>health insurance in <em>2018.</em> That was<br>an increase of <em>1.9 million</em> uninsured<br>people, or <em>0.5</em> percentage point.</p>
  <p class="abs note" style="left:562px;top:974px">In 2017, the number of people without health insurance<br>increased to <b>28.0 million</b>, up from <b>27.3 million</b> the year<br>before, according to the latest Civic Household Census<br>data released today.</p>

  <!-- Fact 2 -->
  <div class="abs num" style="left:108px;top:1184px">2</div>
  <div class="abs rule" style="left:84px;top:1313px;width:376px"></div>
  <p class="abs fact" style="left:81px;top:1345px">Working-age adults made up a<br>much larger share of the uninsured<br>population than any other age group.<br>In fact, most uninsured people <em>(84.6</em><br><em>percent)</em> were <em>19- to 64-year-olds.</em></p>
  <div class="abs art" role="img" aria-label="Illustration of a group of five older adults standing together" style="left:690px;top:1262px;width:425px;height:275px;background:linear-gradient(180deg,#e9eef0,#b9c6cc)"></div>

  <!-- Fact 3 -->
  <div class="abs teal-band"></div>
  <div class="abs art" role="img" aria-label="Illustration of a checklist clipboard with a shield badge and a crossing line" style="left:80px;top:1640px;width:425px;height:420px;background:linear-gradient(150deg,#3f59c9,#f7f7f7)"></div>
  <div class="abs num" style="left:610px;top:1638px;-webkit-text-stroke-color:var(--ink)">3</div>
  <div class="abs rule" style="left:584px;top:1767px;width:393px;background:var(--ink)"></div>
  <p class="abs fact" style="left:579px;top:1798px;line-height:34px">The two largest groups in that age range<br>are <em>26 to 34</em> year olds and <em>35 to 44</em> year<br>olds. About <em>1 in 4</em> uninsured people were<br><em>26 to 34</em> years old, and about <em>1 in 5</em><br>people ages <em>34 to 44.</em></p>

  <!-- Fact 4 -->
  <div class="abs num" style="left:110px;top:2104px">4</div>
  <div class="abs rule" style="left:84px;top:2233px;width:400px"></div>
  <p class="abs fact" style="left:84px;top:2270px;line-height:34px">Over half of all people without health<br>insurance coverage were male <em>(54.6</em><br><em>percent)</em>, even though the U.S.<br>population has more women than men.</p>
  <div class="abs" role="img" aria-label="Illustration of a handshake over an insurance policy inside a red prohibition sign" style="left:706px;top:2090px;width:408px;height:408px;border-radius:50%;border:22px solid #e8282c;background:radial-gradient(circle,#eaf4e6,#cfe3c6)"></div>

  <!-- Fact 5 -->
  <div class="abs num" style="left:555px;top:2511px">5</div>
  <div class="abs rule" style="left:184px;top:2640px;width:820px"></div>
  <div class="abs stat-box" style="left:120px;top:2685px">
    <div class="lead">ABOUT</div>
    <div class="big">4 IN 10</div>
    <div class="tail">UNINSURED PEOPLE<br>WERE NON-HISPANIC<br>WHITE</div>
  </div>
  <div class="abs vs">VS</div>
  <div class="abs stat-box" style="left:691px;top:2685px">
    <div class="lead">WHILE NEARLY</div>
    <div class="big">6 IN 10</div>
    <div class="tail">PEOPLE IN THE UNITED<br>STATES WERE<br>NON-HISPANIC WHITE.</div>
  </div>

  <!-- Fact 6 -->
  <div class="abs art" role="img" aria-label="Illustration of an insurance document under an umbrella with medical staff, pills, cash and a shield" style="left:61px;top:3195px;width:462px;height:415px;background:linear-gradient(160deg,#7cc7e8,#6b4fa8)"></div>
  <div class="abs num" style="left:655px;top:3213px">6</div>
  <div class="abs rule" style="left:626px;top:3342px;width:380px"></div>
  <p class="abs fact" style="left:622px;top:3380px;font-size:28px;line-height:38px">Other races and ethnic groups<br>made up the majority of the<br>uninsured population but less<br>than half <em>(39.3 percent)</em> of the<br>total population.</p>

  <svg class="abs" style="left:0;top:3620px" width="1200" height="339" viewBox="0 0 1200 339" aria-hidden="true">
    <defs>
      <linearGradient id="footGrad" x1="0" y1="0" x2="0" y2="1">
        <stop offset="0" stop-color="#5fd0fa"/>
        <stop offset="1" stop-color="#22aef0"/>
      </linearGradient>
    </defs>
    <path d="M0 30C300 0 500 60 700 40C900 20 1050 0 1200 20V339H0Z" fill="url(#footGrad)"/>
  </svg>
  <p class="abs closing">The uninsured were disproportionately<br>concentrated in the South.</p>

</main>
</body>
</html>
```